Energy trading company (Voltrisa) needs a business card

We need a business card for a company based in Central America. Our main purpose is trading energy . We already have the logo but we need some good creativity to design a high impact business card. Colors blue, orange, green can be used or we would like to see good combinatios with our logo

Target Market(s)

Energy

Industry/Entity Type

Power Generation

Contact Information for Business Card

Logo , headquarters , name, background

Font styles to use
Serif
Sans Serif

Colors

Designer to choose colors to be used in the design.

Requirements
Must have
• it must have a fresh and clean view
Nice to have
• good backgrounds that combine with the logo
Should not have
• too much words

```html
<!DOCTYPE html>
<html lang="en">
<head>
<meta charset="UTF-8">
<title>Voltrisa Business Card</title>
<link href="https://fonts.googleapis.com/css2?family=Catamaran:wght@500&family=Saira+Condensed:wght@600&family=Roboto:wght@400&display=swap" rel="stylesheet">
<style>
  :root {
    --stage: #1c1c1c;
    --card-top: #3a3a3a;
    --card-mid: #1d1d1d;
    --card-bottom: #131313;
    --orange: #ee8a1d;
    --text-light: #f2f2f2;
    --pattern-light: #2c2c2c;
    --pattern-dark: #151515;
  }
  * { margin: 0; padding: 0; box-sizing: border-box; }
  html, body { width: 1200px; height: 909px; overflow: hidden; }
  body { background: var(--stage); position: relative; font-family: "Roboto", sans-serif; }

  .card {
    position: absolute;
    top: 166px;
    width: 348px;
    height: 576px;
    border-radius: 14px;
    overflow: hidden;
  }
  .card-front {
    left: 226px;
    background: linear-gradient(180deg, var(--card-top) 0%, var(--card-mid) 45%, var(--card-bottom) 100%);
  }
  .card-back { left: 626px; }

  .brand-dot {
    position: absolute;
    left: 118px;
    top: 70px;
    width: 110px;
    height: 110px;
    border-radius: 50%;
    background: var(--orange);
  }
  .brand-name {
    position: absolute;
    left: 0;
    width: 100%;
    top: 200px;
    text-align: center;
    font-family: "Catamaran", sans-serif;
    font-weight: 500;
    font-size: 58px;
    line-height: 1;
    color: var(--orange);
    letter-spacing: 0.5px;
  }

  .person-name {
    position: absolute;
    left: 38px;
    top: 344px;
    font-family: "Saira Condensed", sans-serif;
    font-weight: 600;
    font-size: 24px;
    line-height: 1.2;
    color: var(--orange);
  }
  .person-title {
    position: absolute;
    left: 38px;
    top: 373px;
    font-size: 15px;
    color: var(--text-light);
  }

  .contact-list { position: absolute; left: 38px; top: 417px; list-style: none; }
  .contact-item {
    display: flex;
    align-items: center;
    height: 22px;
    font-size: 15px;
    color: var(--text-light);
  }
  .contact-icon { width: 14px; height: 14px; margin-right: 15px; fill: var(--orange); }

  .address {
    position: absolute;
    left: 38px;
    top: 489px;
    font-size: 15px;
    line-height: 21px;
    color: var(--text-light);
  }

  .back-texture {
    position: absolute;
    inset: 0;
    background: radial-gradient(ellipse at 30% 20%, var(--pattern-light) 0%, var(--pattern-dark) 80%);
  }
  .back-brand {
    position: absolute;
    left: 204px;
    top: 380px;
    font-family: "Catamaran", sans-serif;
    font-weight: 500;
    font-size: 24px;
    line-height: 1;
    color: var(--orange);
  }
</style>
</head>
<body>
  <section class="card card-front">
    <div class="brand-dot"></div>
    <div class="brand-name">VOLTRISA</div>

    <div class="person-name">Marco Duarte Ruiz</div>
    <div class="person-title">Managing Director</div>

    <ul class="contact-list">
      <li class="contact-item">
        <svg class="contact-icon" viewBox="0 0 16 16" aria-hidden="true"><path d="M1 5c0-2 3-3 7-3s7 1 7 3v1h-3V5H4v1H1zM4 7h8l2 6H2z"/></svg>
        506-240-3817
      </li>
      <li class="contact-item">
        <svg class="contact-icon" viewBox="0 0 16 16" aria-hidden="true"><path d="M1 3h14v10H1zM2 4l6 5 6-5v1l-6 5-6-5z" fill-rule="evenodd"/></svg>
        m.duarte@voltrisa.net
      </li>
      <li class="contact-item">
        <svg class="contact-icon" viewBox="0 0 16 16" aria-hidden="true"><circle cx="8" cy="8" r="6.5" fill="none" stroke="#ee8a1d" stroke-width="1.5"/><path d="M1.5 8h13M8 1.5v13" stroke="#ee8a1d" stroke-width="1.2"/><ellipse cx="8" cy="8" rx="3" ry="6.5" fill="none" stroke="#ee8a1d" stroke-width="1.2"/></svg>
        www.voltrisa.net
      </li>
    </ul>

    <div class="address">418 Avenida Central, Sabana,<br>San José, CR 10108</div>
  </section>

  <section class="card card-back">
    <div class="back-texture" role="img" aria-label="Tonal repeating brand pattern in dark grey"></div>
    <div class="back-brand">VOLTRISA</div>
  </section>
</body>
</html>
```